Business Card Design - Corporate

Create a sleek elegant business card layout while suggesting a color scheme. Convey cutting edge technology while maintaining a corporate feel that is easily readable.

Company designs and manufactures consumer electronic products for mass retail that are mainly app driven.

(vector logo and die-line provided)

Target Market(s)

Corporate level, tech industry.

Industry/Entity Type

Business

Contact Information for Business Card

Generic Info:

Name
Title
email
address
phone 1
phone 2
website (vantorelle.com) on back

Font styles to use
Sans Serif

Requirements
Must have
• At least 2 colors + white on one side.
Nice to have
• Solid suggestion on color for logo and overall design. Color flood on back of card.
Should not have
• background texture like... marble, stone, patterns or circuit boards

```html
<!DOCTYPE html>
<html lang="en">
<head>
<meta charset="utf-8">
<title>Vantorelle Business Card</title>
<link href="https://fonts.googleapis.com/css2?family=Open+Sans:wght@400;700&display=swap" rel="stylesheet">
<style>
  :root {
    --stage: #5b5b5b;
    --card-dark: #3a3a3c;
    --brand-blue: #0a6bb0;
    --card-white: #ffffff;
    --text-light: #ffffff;
    --text-muted: #9a9a9c;
    --wordmark-dark: #3a3a3c;
  }
  * { box-sizing: border-box; margin: 0; padding: 0; }
  html, body {
    width: 1200px; height: 1200px; overflow: hidden;
    background: var(--stage);
    font-family: "Open Sans", sans-serif;
  }
  .sheet {
    width: 1200px; height: 1200px;
    display: flex; flex-direction: column;
    align-items: center; justify-content: center; gap: 38px;
  }
  .card {
    position: relative;
    width: 960px; height: 541px;
    border-radius: 10px;
    overflow: hidden;
  }
  .card--front { background: var(--card-dark); }
  .card--back {
    background: var(--card-white);
    display: flex; align-items: center; justify-content: center;
  }
  .front-sweep { position: absolute; inset: 0; }
  .front-wordmark {
    position: absolute; left: 60px; top: 446px;
    color: var(--text-light);
    font-size: 28px; font-weight: 400; letter-spacing: 6px;
  }
  .contact-block {
    position: absolute; left: 463px; top: 150px;
    color: var(--text-light);
  }
  .contact-name { font-size: 39px; font-weight: 700; line-height: 1.1; }
  .contact-position {
    font-size: 24px; color: var(--text-muted); line-height: 1.2;
    text-transform: uppercase;
  }
  .contact-address { margin-top: 30px; font-size: 30px; line-height: 1.22; }
  .contact-lines { margin-top: 22px; list-style: none; }
  .contact-lines li {
    display: flex; align-items: center; gap: 12px;
    font-size: 30px; line-height: 37px;
  }
  .contact-icon { width: 24px; height: 24px; flex: none; }
  .back-wordmark {
    color: var(--wordmark-dark);
    font-size: 72px; font-weight: 400; letter-spacing: 12px;
  }
</style>
</head>
<body>
<main class="sheet">
  <section class="card card--front" aria-label="Card front">
    <svg class="front-sweep" viewBox="0 0 960 541" preserveAspectRatio="none" aria-hidden="true">
      <path d="M0,254 C60,320 125,336 210,336 C300,380 385,470 452,541 L0,541 Z" fill="var(--brand-blue)"/>
    </svg>
    <div class="front-wordmark">VANTORELLE</div>
    <div class="contact-block">
      <p class="contact-name">Name Here</p>
      <p class="contact-position">Position</p>
      <p class="contact-address">2740 Marlow Ave, Suite 4410<br>Fairbrook, CA 94610, USA</p>
      <ul class="contact-lines">
        <li>
          <svg class="contact-icon" viewBox="0 0 24 24" aria-hidden="true"><rect x="6" y="1.5" width="12" height="21" rx="2" fill="none" stroke="#fff" stroke-width="2"/><circle cx="12" cy="19" r="1.2" fill="#fff"/></svg>
          (000) 000-0000
        </li>
        <li>
          <svg class="contact-icon" viewBox="0 0 24 24" aria-hidden="true"><circle cx="12" cy="12" r="10.5" fill="none" stroke="#fff" stroke-width="1.8"/><path d="M8 6.5l2 2.2-1.2 1.6c.8 1.8 2.1 3.1 3.9 3.9l1.6-1.2 2.2 2-1.4 1.9c-4.2-.6-7.6-4-8.2-8.2z" fill="#fff"/></svg>
          (415) 628-3190
        </li>
        <li>
          <svg class="contact-icon" viewBox="0 0 24 24" aria-hidden="true"><rect x="2" y="5.5" width="20" height="13" fill="none" stroke="#fff" stroke-width="1.8"/><path d="M2 5.5l10 7.5 10-7.5M2 18.5l7.5-6.5M22 18.5l-7.5-6.5" fill="none" stroke="#fff" stroke-width="1.6"/></svg>
          info@vantorelle.com
        </li>
        <li>
          <svg class="contact-icon" viewBox="0 0 24 24" aria-hidden="true"><circle cx="12" cy="12" r="10" fill="none" stroke="#fff" stroke-width="1.8"/><ellipse cx="12" cy="12" rx="4.5" ry="10" fill="none" stroke="#fff" stroke-width="1.5"/><path d="M2 12h20M4 7h16M4 17h16" stroke="#fff" stroke-width="1.5"/></svg>
          www.vantorelle.com
        </li>
      </ul>
    </div>
  </section>

  <section class="card card--back" aria-label="Card back">
    <div class="back-wordmark">VANTORELLE</div>
  </section>
</main>
</body>
</html>
```